Website Design Project for Beauty & Wellness Professionals

As background information, I have a website that is focused on Beauty & Wellness Professionals:
- Job Search (www.trilhavelora.com)
- Business Classifieds (negocios.trilhavelora.com)
- Freelancer Classifieds (freelancer.trilhavelora.com)
- Course Reviews (cursos.trilhavelora.com)

All those websites use standard templates.

I need a DESIGN for the HOME PAGE (no coding) of the Website Platform that consolidates the four platforms under the same design.

Website designs that we like:
- quovenda.com
- mirtelpeek.com

Target Market(s)

Brazilian Professionals from Beauty & Wellness sector

Industry/Entity Type

Business

Requirements
Must have
• Website designs that we like:
- quovenda.com
- mirtelpeek.com

```html
<!DOCTYPE html>
<html lang="pt-BR">
<head>
<meta charset="utf-8">
<title>Trilha Velora – Home</title>
<link href="https://fonts.googleapis.com/css2?family=Arimo:wght@400;700&display=swap" rel="stylesheet">
<style>
:root{
  --teal:#2a8fa6;
  --nav-top:#5a5a5a;
  --nav-bottom:#3a3a3a;
  --ink:#222;
  --muted:#555;
  --line:#9a9a9a;
  --panel:#ebebeb;
  --white:#fff;
  --red:#f0525a;
  --green:#5cc77a;
  --blue:#5a96d0;
  --orange:#f6b35e;
  --fb-blue:#4e6dae;
  --tab-grey:#bdbdbd;
}
*{box-sizing:border-box;margin:0;padding:0}
html,body{width:1200px;height:2609px;overflow:hidden}
body{position:relative;background:var(--panel);font-family:"Arimo",Arial,sans-serif;color:var(--ink)}
.abs{position:absolute}
.header{left:0;top:0;width:1200px;height:132px;background:var(--white)}
.brand{left:0;width:1200px;top:30px;text-align:center}
.brand-mark{display:block;margin:0 auto 12px;width:46px;height:46px;border-radius:50%;background:var(--teal)}
.brand-name{font-size:32px;color:var(--teal);font-weight:400}
.nav{left:0;top:132px;width:1200px;height:51px;background:linear-gradient(var(--nav-top),var(--nav-bottom));display:flex;align-items:center;color:#fff;font-size:15.5px}
.nav a{color:#fff;text-decoration:none;margin-left:9px;margin-right:2px}
.nav .right{margin-left:auto;display:flex;gap:20px;padding-right:30px}
.hero{left:0;top:183px;width:1200px;height:633px;background:linear-gradient(100deg,#7fa24a 0%,#6f9440 35%,#c4a48a 50%,#efe9e4 70%,#fff 100%)}
.search{left:164px;top:673px;width:876px;height:62px;border-radius:31px;background:rgba(150,150,150,.55);}
.search .jobs{left:30px;top:20px;font-size:17px;color:#222}
.search .field{top:6px;width:274px;height:52px;background:#fff;border:1px solid #ddd}
.search .btn{left:754px;top:4px;width:122px;height:54px;border-radius:27px;background:var(--orange);color:#fff;font-weight:700;font-size:20px;display:flex;align-items:center;justify-content:center}
.cats{left:0;top:816px;width:1200px;height:138px;background:var(--white);box-shadow:0 8px 12px rgba(0,0,0,.2)}
.cat-links{font-size:13px;color:#444;line-height:22px}
.section-label{font-size:19px;color:#444}
.rule{height:1px;background:var(--line)}
.job{left:0;width:637px}
.tag{left:4px;width:92px;height:30px;color:#fff;font-size:12px;line-height:13px;text-align:center;display:flex;align-items:center;justify-content:center}
.tag.reg{background:var(--red)}.tag.auto{background:var(--green)}.tag.phase{background:var(--blue)}
.job-title{left:114px;font-size:16px;font-weight:700;color:#333;width:500px;line-height:24px}
.job-meta{left:114px;font-size:13px;color:#333;width:500px;line-height:22px}
.advert{left:719px;top:1080px;width:396px;height:131px;background:#fff;border-radius:12px;overflow:hidden}
.advert-head{height:54px;background:var(--fb-blue);color:#fff;font-weight:700;font-size:19px;display:flex;align-items:center;justify-content:center}
.advert-body{text-align:center;color:#555;font-weight:700;font-size:19px;margin-top:25px}
.filter{left:725px;top:1300px;width:388px}
.filter-tabs{display:flex;height:56px}
.filter-tabs div{width:110px;display:flex;align-items:center;justify-content:center;font-size:18px;font-weight:700}
.filter-tabs .on{background:#fff;color:#444}.filter-tabs .off{background:var(--tab-grey);color:#fff;width:110px}
.filter-row{height:47px;background:#fff;border-top:1px solid #ddd;display:flex;align-items:center;justify-content:space-between;padding:0 20px 0 16px;color:#999;font-size:18px}
.follow-col{left:0;top:1671px;width:637px;height:838px;background:#f9f9f9}
.follow{left:168px;width:437px}
.follow h3{font-size:28px;font-weight:700;color:#222}
.follow p{font-size:16px;color:#777;margin-top:4px}
.follow .ico{position:absolute;right:4px;top:-6px;width:74px;height:74px;border-radius:50%}
.news{left:218px;top:2332px;width:335px;height:105px;background:#e6edf5;border:1px solid #c6d4e2;font-size:13px;color:#555;padding:10px 8px}
.news input{width:180px;height:26px;border:1px solid #999;margin-left:8px;vertical-align:middle}
.news button{display:block;margin:12px auto 0;font:14px "Arimo",Arial,sans-serif;padding:3px 8px;border:1px solid #888;background:#f2f2f2}
.course-text{left:660px;width:222px;font-size:13px;line-height:21px;color:#333}
.course-ad{left:902px;width:264px;height:266px;background:#fff;overflow:hidden}
.course-photo{height:160px}
.course-copy{padding:10px 12px;font-size:11px;line-height:14px;color:#222}
.course-cta{margin-top:8px;display:flex;justify-content:space-between;align-items:center}
.course-cta span{background:#e84d1c;color:#fff;font-weight:700;font-size:11px;padding:6px 10px}
.course-cta b{font-size:14px;color:#444}
.footer{left:0;top:2509px;width:1200px;height:100px;background:#fff;text-align:center;font-size:13px;color:#444;line-height:22px;padding-top:16px}
</style>
</head>
<body>
<header class="abs header">
  <div class="abs brand"><span class="brand-mark"></span><span class="brand-name">Trilha Velora</span></div>
</header>
<nav class="abs nav">
  <a>Home</a><a>BLOG</a><a>For Professionals</a><a>For Business</a><a>Events &amp; Partners</a><a>About Us</a><a>Contact Us</a>
  <div class="right"><a>Advertise JOB VACANCY</a><a>Log In/ Register</a></div>
</nav>
<div class="abs hero" role="img" aria-label="Photo of a red-haired woman lying relaxed on the grass"></div>
<div class="abs search">
  <span class="abs jobs">Jobs ▼</span>
  <span class="abs field" style="left:136px"></span>
  <span class="abs field" style="left:428px"></span>
  <span class="abs btn">SEARCH</span>
</div>
<div class="abs cats">
  <div class="abs cat-links" style="left:201px;top:44px">Job Vacancies - Beauty:&nbsp; Aux Hairdresser &nbsp;|&nbsp; Aux Escovista &nbsp;|&nbsp; Hairdresser &nbsp;|&nbsp; epilator &nbsp;|&nbsp; Manicure &nbsp;|&nbsp; Makeup &nbsp;|&nbsp; Eyebrow Designer<br>Job Vacancies - Health and Wellness:&nbsp; Esthetician &nbsp;|&nbsp; Massage Therapist &nbsp;|&nbsp; Podiatrist &nbsp;|&nbsp; Physiotherapist &nbsp;|&nbsp; Nurse</div>
</div>

<div class="abs section-label" style="left:3px;top:992px">FEATURED</div>
<div class="abs section-label" style="left:3px;top:1032px;font-weight:700;font-size:18px">Latest Job Vacancies</div>
<svg class="abs" style="left:594px;top:1027px" width="26" height="26" viewBox="0 0 26 26"><rect width="26" height="26" rx="4" fill="#f08a24"/><circle cx="7" cy="19" r="2.6" fill="#fff"/><path d="M5 11a10 10 0 0 1 10 10M5 5a16 16 0 0 1 16 16" stroke="#fff" stroke-width="3" fill="none"/></svg>
<div class="abs rule" style="left:0;top:1069px;width:1200px"></div>

<div class="abs job" style="top:1070px">
  <span class="abs tag reg" style="top:10px">Registered<br>(CTL)</span>
  <div class="abs job-title" style="top:6px">Auxiliar Cabeleireiro (MASC/FEM.) – Maison Lirelle – São<br>(Bernardo do Campo (SP</div>
  <div class="abs job-meta" style="top:56px">SALÃO MAISON LIRELLE SHOPP CENTRAL-SBC-SP – Publicado<br>por Adelina</div>
</div>
<div class="abs rule" style="left:0;top:1181px;width:637px"></div>
<div class="abs job" style="top:1182px">
  <span class="abs tag reg" style="top:10px">Registered<br>(CTL)</span>
  <div class="abs job-title" style="top:8px">(Esteticista Facial e Corporal – Curicica – Rio de Janeiro (RJ</div>
  <div class="abs job-meta" style="top:36px">Bruma Spa – Publicado por Bruma Spa</div>
</div>
<div class="abs rule" style="left:0;top:1250px;width:637px"></div>
<div class="abs job" style="top:1251px">
  <span class="abs tag auto" style="top:12px">Autonomous</span>
  <div class="abs job-title" style="top:8px">(Auxiliar de Cabeleireiro – Vila Rosália – Guarulhos (SP</div>
  <div class="abs job-meta" style="top:36px">Belissara Cabelo e Estética – Publicado por belissara</div>
</div>
<div class="abs rule" style="left:0;top:1322px;width:637px"></div>
<div class="abs job" style="top:1323px">
  <span class="abs tag reg" style="top:10px">Registered<br>(CTL)</span>
  <div class="abs job-title" style="top:8px">(Estoquista – Maison Lirelle – São Bernardo do Campo (SP</div>
  <div class="abs job-meta" style="top:36px">Adelina – Publicado por Adelina</div>
</div>
<div class="abs rule" style="left:0;top:1397px;width:637px"></div>
<div class="abs job" style="top:1398px">
  <span class="abs tag auto" style="top:12px">Autonomous</span>
  <div class="abs job-title" style="top:6px">Hairdresser and Hairdresser Assistant - Campo Belo - São Paulo<br>((SP</div>
  <div class="abs job-meta" style="top:58px">Ana Werle – Posted by Ana Werle</div>
</div>
<div class="abs rule" style="left:0;top:1490px;width:637px"></div>
<div class="abs job" style="top:1491px">
  <span class="abs tag phase" style="top:12px">Phase</span>
  <div class="abs job-title" style="top:6px">Trainee in aesthetic facial and body - Spa - São Paulo<br>((SP</div>
  <div class="abs job-meta" style="top:58px">RV SPA - Posted by sparv</div>
</div>
<div class="abs rule" style="left:0;top:1589px;width:1200px"></div>
<div class="abs job" style="top:1590px">
  <span class="abs tag reg" style="top:8px">Registered<br>(CTL)</span>
  <div class="abs job-title" style="top:8px">(Stockist - Maison Lirelle - São Bernardo do Campo (SP</div>
  <div class="abs job-meta" style="top:36px">Adelina - Posted by Adelina</div>
</div>
<div class="abs" style="left:566px;top:1652px;font-size:12px;color:#333">NEXT&gt;&gt;</div>
<div class="abs rule" style="left:0;top:1668px;width:637px"></div>

<div class="abs advert"><div class="advert-head">Advertise Job Vacancy</div><div class="advert-body">Advertise vacancy FREE</div></div>
<div class="abs rule" style="left:637px;top:1250px;width:563px"></div>
<div class="abs filter">
  <div class="filter-tabs"><div class="on">Search by</div><div class="off">Tags</div></div>
  <div class="filter-row"><span>Job Type</span><span>&gt;</span></div>
  <div class="filter-row"><span>Salary Job</span><span>&gt;</span></div>
  <div class="filter-row"><span>Job Category</span><span>&gt;</span></div>
  <div class="filter-row"><span>Published Date</span><span>&gt;</span></div>
</div>

<div class="abs follow-col"></div>
<div class="abs rule" style="left:168px;top:1747px;width:437px;background:#ccc"></div>
<div class="abs follow" style="top:1795px"><h3>Subscribe</h3><p>Receive the latest jobs</p><span class="ico" style="background:#f07a22"></span></div>
<div class="abs rule" style="left:168px;top:1893px;width:437px;background:#ccc"></div>
<div class="abs follow" style="top:1922px"><h3>Follow Us</h3><p>Come join us on Trilo</p><span class="ico" style="background:#5bb0e6"></span></div>
<div class="abs rule" style="left:168px;top:2003px;width:437px;background:#ccc"></div>
<div class="abs follow" style="top:2032px"><h3>Follow us</h3><p>Come join us on Circulo+</p><span class="ico" style="background:#8a8a8a"></span></div>
<div class="abs rule" style="left:168px;top:2128px;width:437px;background:#ccc"></div>
<div class="abs follow" style="top:2158px"><h3>Take part!</h3><p>Be part of our network on Mural</p><span class="ico" style="background:#3b5b9a"></span></div>
<div class="abs rule" style="left:168px;top:2271px;width:437px;background:#ccc"></div>
<div class="abs" style="left:221px;top:2310px;font-size:19px;font-weight:700;color:#222">Subscribe Trilha Velora</div>
<div class="abs news">
  <div style="margin-bottom:8px">Get latest Job Vacancies &amp; News.</div>
  <div>Email Address<input type="text" aria-label="Email Address"></div>
  <button type="button">Subscribe!</button>
</div>

<div class="abs" style="left:904px;top:1640px;font-size:23px;color:#333">Online Courses Aprendiz</div>
<div class="abs course-text" style="top:1718px">The course of Makeup Techniques brings updated methods of makeup, with an emphasis on visagism and with different ethnic styles. The course also includes innovations in the areas of care, hygiene and organization to provide service salon,</div>
<div class="abs course-text" style="top:2004px">O curso de cabeleireiro de Renato Falcão pode revolucionar o seu Studio. Além de técnicas de corte incríveis para diversos grupos étnicos e biótipos, dicas de visagismo, avaliação do cabelo e finalização, Renato fala sobre aspectos</div>
<div class="abs course-ad" style="top:1719px">
  <div class="course-photo" role="img" aria-label="Photo of makeup brushes with pink powder" style="background:linear-gradient(135deg,#c98aa0,#8c5a6c 60%,#3d2a33)"></div>
  <div class="course-copy">Seja um profissional mais qualificado, invista na sua carreira e se prepare para o mercado de trabalho. Matricule-se no curso.
    <div class="course-cta"><span>EXPERIMENTE GRÁTIS</span><b>Aprendiz</b></div></div>
</div>
<div class="abs course-ad" style="top:2008px">
  <div class="course-photo" role="img" aria-label="Photo of a hairdresser cutting hair in a salon" style="background:linear-gradient(135deg,#e7c7a4,#b98660 55%,#6e4a35)"></div>
  <div class="course-copy">Seja um profissional mais qualificado, invista na sua carreira e se prepare para o mercado de trabalho. Matricule-se no curso.
    <div class="course-cta"><span>EXPERIMENTE GRÁTIS</span><b>Aprendiz</b></div></div>
</div>

<footer class="abs footer">
  Job Vacancies - Beauty:&nbsp; Aux Hairdresser &nbsp;|&nbsp; Aux Escovista &nbsp;|&nbsp; Hairdresser &nbsp;|&nbsp; epilator &nbsp;|&nbsp; Manicure &nbsp;|&nbsp; Makeup &nbsp;|&nbsp; Eyebrow Designer<br>
  Job Vacancies - Health and Wellness:&nbsp; Esthetician &nbsp;|&nbsp; Massage Therapist &nbsp;|&nbsp; Podiatrist &nbsp;|&nbsp; Physiotherapist &nbsp;|&nbsp; Nurse<br>
  <span style="display:inline-block;margin-top:8px">Copyright 2013 @ Trilha Velora - Your Community for Professionals and Companies Beauty, Aesthetics and Wellness</span>
</footer>
</body>
</html>
```